Card for modern wood artisan that builds log homes and timber frames.

Design a card with catchy imagery. With a quick list of things I build and services I offer.

I'd like an English side and a french side. I can provide the text.

I am basically a guy that builds log homes and timber frames , but I am very eco friendly oriented.

I use only eco friendly products to limit my carbon footprint.
I want the client to feel as if they are hiring a good smart builder.

I have been building for a while but just starting out to market myself out there , not just work for other companies. Starting
My own thing legitimately.

I am very conscientious, and I take care of the work I do. I am trying to bring a new age, modern feel to an old profession.

Reason: I am not completely satisfied with A model yet, looking for that masculin rustic artistic design that I havent completely found yet. Thank you for your sumbissions.

Target Market(s)

People looking to hire a builder to design and build their projects.
And contractors that want to hire a quality subcontractor for their jobs.

Industry/Entity Type

Construction

Contact Information for Business Card

I want my logo on it, that I had designed here.
And a list of services I provide.

With my phone number, website adress and Email.

Requirements
Must have
• Artful presentation,
• Eco friendly feel
• I love trees.

```html
<!DOCTYPE html>
<html lang="en">
<head>
<meta charset="utf-8">
<title>Timberlyn — Business Card</title>
<link rel="stylesheet" href="https://fonts.googleapis.com/css2?family=Cedarville+Cursive&family=Shadows+Into+Light+Two&display=swap">
<style>
  :root {
    --backdrop: #6e7674;
    --linen: #ece8e1;
    --wood-light: #c9772a;
    --wood-mid: #a8561a;
    --wood-dark: #7a3a0f;
    --tree-gold: #e39a22;
    --tree-deep: #c97a12;
    --ink: #1b1b1b;
    --ink-blue: #1f3f92;
    --ink-brown: #6a3315;
    --ink-orange: #e39a22;
  }
  * { box-sizing: border-box; margin: 0; padding: 0; }
  html, body { width: 1200px; height: 900px; overflow: hidden; }
  body { background: var(--backdrop); position: relative; }

  .card {
    position: absolute;
    left: 260px;
    width: 680px;
    height: 390px;
    border-radius: 30px;
    background: var(--linen);
    box-shadow: 0 10px 30px rgba(0,0,0,.3);
    overflow: hidden;
  }
  .card--front { top: 40px; }
  .card--back { top: 470px; }

  .wood {
    position: absolute;
    background: linear-gradient(135deg, var(--wood-light), var(--wood-mid) 55%, var(--wood-dark));
  }
  .card--front .wood--corner { right: 0; top: 0; width: 80px; height: 140px; }
  .card--front .wood--edge { left: 0; top: 175px; width: 60px; height: 140px; }
  .card--back .wood--edge { left: 0; top: 40px; width: 50px; height: 120px; }
  .card--back .wood--corner { right: 0; top: 30px; width: 90px; height: 90px; }

  .tree-art {
    position: absolute;
    left: 170px; top: 55px;
    width: 150px; height: 270px;
    border-radius: 50% 50% 30% 30% / 60% 60% 20% 20%;
    background: radial-gradient(ellipse at 50% 40%, var(--tree-gold), var(--tree-deep) 80%);
    opacity: .9;
  }

  .brand {
    position: absolute;
    left: 95px; top: 165px;
    display: flex; align-items: center; gap: 10px;
    padding: 6px 14px 6px 8px;
    background: var(--linen);
  }
  .brand__square { width: 24px; height: 24px; background: var(--ink); }
  .brand__name {
    font-family: "Shadows Into Light Two", cursive;
    font-size: 28px; color: var(--ink); letter-spacing: 2px; line-height: 1;
  }

  .identity { position: absolute; left: 360px; top: 48px; }
  .identity__name {
    font-family: "Cedarville Cursive", cursive;
    font-size: 26px; color: var(--ink); white-space: nowrap;
  }
  .identity__role {
    font-family: "Shadows Into Light Two", cursive;
    font-size: 14px; color: var(--ink-brown); margin-left: 14px;
  }

  .contact {
    position: absolute;
    display: flex; align-items: center; gap: 8px;
    font-family: "Shadows Into Light Two", cursive;
    font-size: 15px; line-height: 1.1; white-space: nowrap;
  }
  .contact svg { width: 24px; height: 24px; flex: none; }
  .contact--address { left: 380px; top: 125px; color: var(--ink-brown); font-size: 14px; }
  .contact--phone { left: 425px; top: 178px; color: var(--ink-blue); font-size: 18px; letter-spacing: 2px; }
  .contact--email { left: 330px; top: 232px; color: var(--ink); }
  .contact--web { left: 500px; top: 232px; color: var(--ink-blue); }

  .services {
    position: absolute; inset: 0;
    font-family: "Cedarville Cursive", cursive;
  }
  .service { position: absolute; white-space: nowrap; transform: rotate(-8deg); transform-origin: left center; line-height: 1.2; }
  .service--black-1 { left: 80px; top: 140px; font-size: 21px; color: var(--ink); }
  .service--blue-1 { left: 115px; top: 180px; font-size: 23px; color: var(--ink-blue); }
  .service--brown { left: 70px; top: 245px; font-size: 25px; color: var(--ink-brown); }
  .service--black-2 { left: 330px; top: 108px; font-size: 19px; color: var(--ink); }
  .service--blue-2 { left: 335px; top: 185px; font-size: 23px; color: var(--ink-blue); }
  .service__under { border-bottom: 2px solid var(--ink-brown); }

  .mark { position: absolute; }
</style>
</head>
<body>

<section class="card card--front" aria-label="Card front">
  <div class="wood wood--corner" role="img" aria-label="Cut log end grain texture"></div>
  <div class="wood wood--edge" role="img" aria-label="Cut log end grain texture"></div>
  <div class="tree-art" role="img" aria-label="Golden illustrated tree with roots"></div>

  <div class="brand">
    <span class="brand__square"></span>
    <span class="brand__name">TIMBERLYN</span>
  </div>

  <div class="identity">
    <p class="identity__name">Your Name Here</p>
    <p class="identity__role">Co-Founder &amp; CEO</p>
  </div>

  <div class="contact contact--address">
    <svg viewBox="0 0 26 26"><circle cx="13" cy="13" r="13" fill="var(--ink-brown)"/><path d="M13 6a5 5 0 0 0-5 5c0 4 5 9 5 9s5-5 5-9a5 5 0 0 0-5-5z" fill="#fff"/><circle cx="13" cy="11" r="2" fill="var(--ink-brown)"/></svg>
    <span>382 YOUR address<br>your City, your Country</span>
  </div>
  <div class="contact contact--phone">
    <svg viewBox="0 0 26 26"><circle cx="13" cy="13" r="13" fill="var(--ink-blue)"/><rect x="9" y="6" width="8" height="14" rx="1.5" fill="none" stroke="#fff" stroke-width="1.6"/></svg>
    <span>(007) 666-1234</span>
  </div>
  <div class="contact contact--email">
    <svg viewBox="0 0 26 26"><circle cx="13" cy="13" r="13" fill="var(--ink-orange)"/><rect x="7" y="9" width="12" height="8" fill="none" stroke="#fff" stroke-width="1.5"/><path d="M7 9l6 5 6-5" fill="none" stroke="#fff" stroke-width="1.5"/></svg>
    <span>email@address.com</span>
  </div>
  <div class="contact contact--web">
    <svg viewBox="0 0 26 26"><circle cx="13" cy="13" r="13" fill="var(--ink-blue)"/><g fill="none" stroke="#fff" stroke-width="1.4"><circle cx="13" cy="13" r="6.5"/><ellipse cx="13" cy="13" rx="3" ry="6.5"/><path d="M6.5 13h13"/></g></svg>
    <span>yourwebsite.com</span>
  </div>
</section>

<section class="card card--back" aria-label="Card back">
  <div class="wood wood--edge" role="img" aria-label="Cut log end grain texture"></div>
  <div class="wood wood--corner" role="img" aria-label="Cut log end grain texture"></div>

  <div class="services">
    <p class="service service--black-1">Your service here</p>
    <p class="service service--blue-1">Your service here</p>
    <p class="service service--brown">Your <span class="service__under">service</span> here</p>
    <p class="service service--black-2">Your service here</p>
    <p class="service service--blue-2">Your service here</p>

    <svg class="mark" style="left:308px;top:140px" width="45" height="22" viewBox="0 0 45 22" aria-hidden="true">
      <path d="M42 3 L4 18 M4 18 l9 1 M4 18 l5 -7" fill="none" stroke="var(--ink-blue)" stroke-width="1.4" stroke-linecap="round"/>
    </svg>
    <svg class="mark" style="left:310px;top:120px" width="260" height="130" viewBox="0 0 260 130" aria-hidden="true">
      <ellipse cx="130" cy="65" rx="124" ry="32" transform="rotate(-8 130 65)" fill="none" stroke="var(--ink-blue)" stroke-width="1.6"/>
    </svg>
  </div>
</section>

</body>
</html>
```